Wordpress Template Design using existing Logo and Colors

We are wanting a wordpress theme designing for our b2b marketing consultancy business. A comprehesive and elagant design to our current site www.provexlink.com would be good.

Industry/Entity Type

Marketing

Font styles to use
Sans Serif

```html
<!DOCTYPE html>
<html lang="en">
<head>
<meta charset="utf-8">
<title>Provexlink — Strategic Marketing Partner</title>
<link rel="stylesheet" href="https://fonts.googleapis.com/css2?family=Merriweather:wght@400;700&family=Open+Sans:ital,wght@0,400;0,600;0,700;1,400&display=swap">
<style>
:root{
  --red:#e1262d;
  --navy:#1e2a55;
  --ink:#2b2f3a;
  --muted:#7a7f8c;
  --line:#d9dbe3;
  --lavender:#eef0fa;
  --contact-blue:#566a9c;
  --strip:#eeeff2;
  --partner:#a5a9b3;
  --white:#ffffff;
}
*{box-sizing:border-box;margin:0;padding:0}
html,body{width:1200px;height:4680px;overflow:hidden}
body{font-family:"Open Sans",Arial,sans-serif;color:var(--ink);background:var(--white);font-size:15px;line-height:1.6}
.serif{font-family:"Merriweather",Georgia,serif}
a{color:inherit;text-decoration:none}
.btn{display:inline-block;font-size:13px;font-weight:700;letter-spacing:1px;text-transform:uppercase;padding:11px 26px;border:2px solid var(--red)}
.btn-red{background:var(--red);color:var(--white)}
.btn-outline{color:var(--red);background:transparent}

/* header */
.site-header{height:88px;display:flex;align-items:center;padding:0 112px;background:var(--white);position:relative;z-index:2}
.brand{display:flex;align-items:center;gap:10px;font-weight:700;font-size:30px;color:var(--red);letter-spacing:1px}
.brand-dot{width:12px;height:12px;border-radius:50%;background:var(--navy)}
.main-nav{margin-left:auto;display:flex;align-items:center;gap:44px;font-size:15px;font-weight:600;color:var(--ink)}
.main-nav .nav-cta{border:2px solid var(--red);color:var(--red);padding:6px 18px;font-size:14px}

/* hero */
.hero{height:592px;position:relative;display:flex;flex-direction:column;align-items:center;justify-content:center;text-align:center;color:var(--white)}
.hero-photo{position:absolute;inset:0;background:linear-gradient(180deg,#7d8593 0%,#5a6170 45%,#3a3f4a 100%)}
.hero-content{position:relative;padding-top:40px}
.hero h1{font-weight:400;font-size:46px;line-height:1.3}
.hero p{font-size:22px;margin:26px 0 38px}
.hero-actions{display:flex;gap:20px;justify-content:center}
.hero-actions .btn-dark{border-color:#2a2e38;background:rgba(30,34,44,.55);color:var(--white)}

/* trusted */
.trusted{height:88px;background:var(--strip);display:flex;align-items:center;justify-content:space-between;padding:0 40px;color:var(--partner);white-space:nowrap}
.trusted-label{font-size:14px;font-weight:700;color:var(--ink)}
.trusted-name{font-size:26px;font-weight:700;letter-spacing:.5px}

/* about */
.about{height:552px;display:flex;align-items:center;padding:0 140px;gap:200px}
.about-media{position:relative;width:372px;height:320px}
.about-media .frame{position:absolute;left:-14px;top:-14px;width:372px;height:320px;border:2px solid var(--navy)}
.about-media .photo{position:absolute;inset:0;background:linear-gradient(135deg,#dfe3ea,#a9b1bf)}
.about-text{width:340px}
.about-text h2{font-size:24px;color:var(--navy);margin-bottom:22px}
.about-text p{font-size:15px;color:var(--muted);margin-bottom:16px;line-height:1.6}
.about-text .btn{margin-top:6px}

/* services */
.services{height:1200px;position:relative;background:var(--lavender);text-align:center;padding-top:82px}
.services-bg{position:absolute;inset:0;background:linear-gradient(180deg,#f3f4fb 0%,#e6e8f6 50%,#f1f2fa 100%)}
.section-head{position:relative}
.section-head h2{font-size:26px;color:var(--ink);font-weight:700}
.section-head p{font-size:17px;color:var(--muted);margin-top:12px}
.service-grid{position:relative;display:grid;grid-template-columns:repeat(3,280px);gap:40px 32px;justify-content:center;margin-top:46px}
.service-card{background:var(--white);height:376px;text-align:center;position:relative}
.service-card .thumb{height:220px}
.service-card h3{font-size:17px;font-weight:600;margin-top:34px;color:var(--ink)}
.service-card p{font-size:13px;color:var(--muted);padding:8px 40px 0;line-height:1.5}
.service-card .badge{position:absolute;left:50%;top:192px;transform:translateX(-50%);width:52px;height:52px;border-radius:50%;background:var(--red);display:flex;align-items:center;justify-content:center}
.t1{background:linear-gradient(135deg,#e7d9b0,#f3e6bd 40%,#8f8676)}
.t2{background:linear-gradient(135deg,#4b6f93,#c8d3df)}
.t3{background:linear-gradient(135deg,#cfe0ee,#6b93b8)}
.t4{background:linear-gradient(135deg,#2f5d80,#8fb2cf)}
.t5{background:linear-gradient(135deg,#e5e7ec,#9ca6b8)}
.t6{background:linear-gradient(135deg,#0f1d3a,#33537f)}
.services .btn{position:relative;margin-top:48px}

/* testimonials */
.testimonials{height:520px;text-align:center;padding-top:112px;position:relative}
.quote-mark{position:absolute;top:250px;font-family:"Merriweather",Georgia,serif;font-size:280px;line-height:1;color:#eceef2;font-weight:700}
.quote-left{left:180px}
.quote-right{right:180px}
.testimonial{position:relative;margin-top:46px}
.testimonial blockquote{font-size:25px;line-height:1.5;color:var(--ink);max-width:760px;margin:0 auto}
.author{display:flex;align-items:center;justify-content:center;gap:18px;margin-top:40px;text-align:left}
.avatar{width:64px;height:64px;border-radius:50%;background:linear-gradient(135deg,#c9ccd3,#7f8594)}
.author strong{display:block;font-size:16px;color:var(--ink)}
.author span{font-size:13px;color:var(--muted)}
.arrow{position:absolute;top:282px}
.arrow-prev{left:148px}
.arrow-next{right:120px}
.dots{display:flex;justify-content:center;gap:6px;margin-top:30px}
.dots i{width:14px;height:4px;background:#d7d9df}
.dots i.on{background:var(--red)}

/* contact */
.contact{height:720px;position:relative;background:var(--contact-blue);color:var(--white);text-align:center;padding-top:92px}
.contact-map{position:absolute;left:160px;right:160px;top:160px;bottom:120px;background:radial-gradient(ellipse at center,rgba(255,255,255,.10),rgba(255,255,255,0) 70%)}
.contact h2{position:relative;font-size:26px}
.contact .lead{position:relative;font-size:17px;margin-top:12px;opacity:.9}
.contact-form{position:relative;width:760px;margin:66px auto 0;display:grid;grid-template-columns:1fr 1fr;column-gap:60px;row-gap:40px;text-align:left}
.field{border-bottom:1px solid rgba(255,255,255,.8);padding-bottom:16px;font-size:14px}
.field.wide{grid-column:1/3;height:130px}
.form-actions{grid-column:1/3;display:flex;justify-content:flex-end;margin-top:-30px}
.btn-submit{border:2px solid var(--white);color:var(--white);padding:8px 40px;font-size:13px}

/* brochure */
.brochure{height:300px;display:flex;align-items:center;justify-content:space-between;padding:0 120px;border-bottom:1px solid var(--line)}
.brochure h2{font-size:22px;color:var(--ink)}
.brochure p{font-size:14px;color:var(--muted);margin-top:12px;width:620px}
.btn-download{display:flex;align-items:center;gap:10px;border:2px solid var(--navy);color:var(--navy);padding:8px 22px;font-size:13px;font-weight:700}

/* footer */
.site-footer{height:560px;padding:80px 120px 0;display:flex;position:relative}
.footer-about{width:300px}
.footer-about .brand{font-size:26px}
.footer-about p{font-size:13px;color:var(--muted);margin-top:30px;line-height:1.6}
.social{display:flex;gap:14px;margin-top:24px}
.social i{width:26px;height:26px;background:#9aa0ad}
.social i.on{background:var(--red)}
.footer-col{margin-left:108px}
.footer-col h4{font-size:15px;color:var(--red);font-weight:700;margin-bottom:16px}
.footer-col li{list-style:none;font-size:13px;color:var(--muted);line-height:2.1}
.contact-col{margin-left:130px;width:240px;font-size:13px;color:var(--muted);line-height:1.7}
.contact-col h4{font-size:15px;color:var(--red);font-weight:700;margin-bottom:12px}
.contact-col h5{font-size:13px;color:var(--ink);font-weight:700;margin-top:4px}
.contact-col .block{margin-bottom:18px}
.contact-col .email{color:var(--red)}
.footer-bottom{position:absolute;left:0;right:0;bottom:0;height:60px;display:flex;align-items:center;justify-content:space-between;padding:0 120px;font-size:12px;color:var(--muted);border-top:1px solid var(--line)}
.footer-bottom nav{display:flex;gap:20px}
</style>
</head>
<body>

<header class="site-header">
  <a class="brand" href="#"><span>PROVEXLINK</span><span class="brand-dot"></span></a>
  <nav class="main-nav">
    <a href="#">About</a>
    <a href="#">Target Marketing</a>
    <a href="#">Data Management</a>
    <a class="nav-cta" href="#">Contact Us</a>
  </nav>
</header>

<section class="hero">
  <div class="hero-photo" role="img" aria-label="Business team smiling around a meeting table in a bright office"></div>
  <div class="hero-content">
    <h1 class="serif">We Are Your<br>Strategic Marketing Partner</h1>
    <p>Promote your business to next level with Us</p>
    <div class="hero-actions">
      <a class="btn btn-dark" href="#">Learn More</a>
      <a class="btn btn-red" href="#">Contact Us</a>
    </div>
  </div>
</section>

<section class="trusted">
  <span class="trusted-label">Trusted By:</span>
  <span class="trusted-name">DORLANIX</span>
  <span class="trusted-name">Vestrova</span>
  <span class="trusted-name">Kelmora</span>
  <span class="trusted-name">TRUBEXA</span>
  <span class="trusted-name">Zantrel</span>
  <span class="trusted-name">Pomerix</span>
</section>

<section class="about">
  <div class="about-media">
    <div class="frame"></div>
    <div class="photo" role="img" aria-label="Overhead view of colleagues reviewing charts at a white desk"></div>
  </div>
  <div class="about-text">
    <h2 class="serif">You're in a Good Company</h2>
    <p>We are a B2B Data, Analytics and Marketing Consulting Company specialized in harnessing the power of potential data to strengthen connections between decision makers, companies and products.</p>
    <p>We focus on solutions engineered to solve distinct challenges in the data, direct marketing and analytics space.</p>
    <a class="btn btn-outline" href="#" style="text-transform:none;letter-spacing:0;padding:8px 22px">Learn More</a>
  </div>
</section>

<section class="services">
  <div class="services-bg" role="img" aria-label="Faint city skyline washed in pale lavender"></div>
  <div class="section-head">
    <h2 class="serif">Our Services</h2>
    <p>We provide the best solutions for your business to grow</p>
  </div>
  <div class="service-grid">
    <article class="service-card">
      <div class="thumb t1" role="img" aria-label="Glowing light bulb among paper notes"></div>
      <span class="badge"><svg width="24" height="24" viewBox="0 0 24 24" fill="none" stroke="#fff" stroke-width="2"><circle cx="12" cy="12" r="9"/><circle cx="12" cy="12" r="5"/><circle cx="12" cy="12" r="1.5" fill="#fff"/></svg></span>
      <h3>Target Marketing</h3>
      <p>Reach the exact buyers who matter, with precision and care</p>
    </article>
    <article class="service-card">
      <div class="thumb t2" role="img" aria-label="Business partners shaking hands"></div>
      <h3>B2B Database</h3>
      <p>Verified company records kept fresh for steady sales growth</p>
    </article>
    <article class="service-card">
      <div class="thumb t3" role="img" aria-label="Call centre agent wearing a headset"></div>
      <h3>Call Centre</h3>
      <p>Skilled agents handling outreach and support for your brand</p>
    </article>
    <article class="service-card">
      <div class="thumb t4" role="img" aria-label="Analysts working at a laptop with charts"></div>
      <h3>Data Management</h3>
      <p>Clean, organised data ready for every campaign you launch</p>
    </article>
    <article class="service-card">
      <div class="thumb t5" role="img" aria-label="Printed reports and charts on a desk"></div>
      <h3>Data Quality Audit</h3>
      <p>Thorough checks that expose gaps, duplicates and old entries</p>
    </article>
    <article class="service-card">
      <div class="thumb t6" role="img" aria-label="Dark blue digital network visual"></div>
      <h3>Data Processing</h3>
      <p>Fast, accurate handling of large lists for lasting value</p>
    </article>
  </div>
  <a class="btn btn-red" href="#">All Services</a>
</section>

<section class="testimonials">
  <span class="quote-mark quote-left" aria-hidden="true">&ldquo;</span>
  <span class="quote-mark quote-right" aria-hidden="true">&rdquo;</span>
  <div class="section-head">
    <h2 class="serif">Our Testimonials</h2>
    <p>Many of our customers have depended on us since day one</p>
  </div>
  <svg class="arrow arrow-prev" width="24" height="40" viewBox="0 0 24 40"><path d="M20 4 L6 20 L20 36" fill="none" stroke="#c9ccd3" stroke-width="3"/></svg>
  <svg class="arrow arrow-next" width="24" height="40" viewBox="0 0 24 40"><path d="M4 4 L18 20 L4 36" fill="none" stroke="#e1262d" stroke-width="3"/></svg>
  <div class="testimonial">
    <blockquote>&ldquo;I love your system. Data marketing is great. I will refer everyone<br>I know. This is simply unbelievable!&rdquo;</blockquote>
    <div class="author">
      <div class="avatar" role="img" aria-label="Portrait of the client"></div>
      <div><strong>Marcus L. Dalton</strong><span>CEO &amp; VP of Marketing</span></div>
    </div>
    <div class="dots"><i class="on"></i><i></i><i></i></div>
  </div>
</section>

<section class="contact">
  <div class="contact-map" role="img" aria-label="Dotted world map in soft white"></div>
  <h2 class="serif">Contact Us</h2>
  <p class="lead">Get in touch with us today and start promoting your business</p>
  <form class="contact-form">
    <div class="field">Your Name</div>
    <div class="field">Your Email</div>
    <div class="field">Subject</div>
    <div class="field">Your Phone</div>
    <div class="field wide">Message</div>
    <div class="form-actions"><span class="btn btn-submit">Submit</span></div>
  </form>
</section>

<section class="brochure">
  <div>
    <h2 class="serif">Corporate Brochure</h2>
    <p>Learn our leading target marketing and intelligent data management solutions to attain new customers for your niche products and services.</p>
  </div>
  <a class="btn-download" href="#">DOWNLOAD
    <svg width="14" height="14" viewBox="0 0 14 14"><path d="M7 1 V10 M3 6 L7 10 L11 6 M1 13 H13" fill="none" stroke="#1e2a55" stroke-width="2"/></svg>
  </a>
</section>

<footer class="site-footer">
  <div class="footer-about">
    <a class="brand" href="#"><span>PROVEXLINK</span><span class="brand-dot"></span></a>
    <p>We are the primary source of market intelligence for growing firms, helping business leaders throughout Asia and North America find new opportunities.</p>
    <div class="social"><i></i><i></i><i></i><i></i><i class="on"></i></div>
  </div>
  <div class="footer-col">
    <h4 class="serif">Quick Links</h4>
    <ul>
      <li>About Us</li><li>Target Marketing</li><li>B2B Database</li><li>Call Centre</li>
      <li>Demand Generation</li><li>Lead Generation</li><li>Data Management</li>
      <li>Data Quality Audit</li><li>Data Processing</li><li>Data Analytics</li><li>Contact Us</li>
    </ul>
  </div>
  <div class="contact-col">
    <h4 class="serif">Contact Us</h4>
    <div class="block">
      <h5>Global</h5>
      4418 Alder Crest Road Suite 210,<br>Halden, CA 90417-5512, USA<br>+1 (555) 014-2290<br>
      <span class="email">contactus.us@provexlink.com</span><br>Monday – Friday, 9AM – 6PM
    </div>
    <div class="block">
      <h5>Regional</h5>
      38 Marlow Lane, #07-04<br>Keppel Point, Singapore 400118<br>+65 5550 1187<br>
      <span class="email">contactus.sg@provexlink.com</span><br>Monday – Friday, 9AM – 6PM
    </div>
  </div>
  <div class="footer-bottom">
    <span>© 2017 Provexlink. All rights reserved · www.provexlink.com</span>
    <nav><a href="#">Site Map</a><a href="#">Disclaimer</a><a href="#">Privacy Policy</a></nav>
  </div>
</footer>

</body>
</html>
```